Mortgage Broking boutique Business

I’m wanting a revamped look to my existing business card design. I do like the black and silver but happy to have other colours introduced based on your creation. I’ve attached a copy of my current card so you can have a starting point updated details noted brloe. I deal with high net worth individuals so need my card to be sophisticated, classy that gives off a classy vibe

Target Market(s)

High net worth, wealthy

Industry/Entity Type

Mortgage Brokerage

Contact Information for Business Card

Job title: Finance Executive
Phone: +61 7 3287 4419
Mobile: 0471 352 608
Email: marcus@quillbrookcapital.com.au
Web: www.quillbrookcapital.com.au
Address: level 36 Tindale Court, 58 Harwick St Brisbane QLD 4000

Font styles to use
Other font styles liked:
• Helvetica

Colors

Designer to choose colors to be used in the design.

Requirements
Must have
• Use my existing card design as a starting point

```html
<!DOCTYPE html>
<html lang="en">
<head>
<meta charset="utf-8">
<title>Quillbrook Capital – Business Card</title>
<link rel="stylesheet" href="https://fonts.googleapis.com/css2?family=Josefin+Sans:wght@600&family=Inter:wght@300&display=swap">
<style>
  :root {
    --page: #f4f4f4;
    --card: #000000;
    --accent: #c9542a;
    --ink-light: #d9d9d9;
    --rule: #8a8a8a;
  }
  html, body {
    margin: 0;
    width: 1200px;
    height: 1200px;
    overflow: hidden;
    background: var(--page);
  }
  .sheet {
    position: relative;
    width: 1200px;
    height: 1200px;
  }
  .card {
    position: absolute;
    top: 450px;
    width: 527px;
    height: 301px;
    background: var(--card);
    box-shadow: 0 2px 6px rgba(0,0,0,0.15);
  }
  .card--front { left: 49px; }
  .card--back  { left: 624px; }

  .brand {
    position: absolute;
    left: 0;
    right: 0;
    text-align: center;
    font-family: "Josefin Sans", sans-serif;
    font-weight: 600;
    color: var(--accent);
    text-transform: uppercase;
    line-height: 1.1;
  }
  .card--front .brand {
    top: 64px;
    font-size: 24px;
    letter-spacing: 1px;
  }
  .card--back .brand {
    top: 112px;
    font-size: 42px;
    letter-spacing: 2px;
  }

  .person {
    position: absolute;
    left: 22px;
    top: 188px;
    width: 196px;
    text-align: center;
  }
  .person__name {
    display: inline-block;
    font-family: "Josefin Sans", sans-serif;
    font-weight: 600;
    font-size: 19px;
    color: var(--accent);
    letter-spacing: 0.5px;
    text-transform: uppercase;
    white-space: nowrap;
    padding-bottom: 3px;
    border-bottom: 1px solid var(--accent);
  }
  .person__title {
    margin-top: 5px;
    font-family: "Josefin Sans", sans-serif;
    font-weight: 600;
    font-size: 9px;
    color: var(--ink-light);
    letter-spacing: 1.5px;
    text-transform: uppercase;
  }

  .divider {
    position: absolute;
    left: 245px;
    top: 189px;
    width: 1px;
    height: 89px;
    background: var(--rule);
  }

  .contact {
    position: absolute;
    left: 280px;
    top: 186px;
    margin: 0;
    padding: 0;
    list-style: none;
    font-family: "Inter", sans-serif;
    font-weight: 300;
    font-size: 12.5px;
    color: var(--ink-light);
    line-height: 15px;
  }
  .contact__item {
    display: flex;
    align-items: flex-start;
    margin-bottom: 6px;
  }
  .contact__icon {
    width: 12px;
    height: 12px;
    margin-top: 1px;
    margin-right: 9px;
    flex: none;
    fill: var(--accent);
  }

  .web {
    position: absolute;
    left: 0;
    right: 0;
    top: 265px;
    text-align: center;
    font-family: "Inter", sans-serif;
    font-weight: 300;
    font-size: 16px;
    color: var(--accent);
    letter-spacing: 0.3px;
  }
</style>
</head>
<body>
<main class="sheet">

  <section class="card card--front">
    <div class="brand">Quillbrook Capital</div>

    <div class="person">
      <div class="person__name">Marcus Whitlow</div>
      <div class="person__title">Finance Executive</div>
    </div>

    <div class="divider"></div>

    <ul class="contact">
      <li class="contact__item">
        <svg class="contact__icon" viewBox="0 0 12 12"><path d="M6 0a4 4 0 0 0-4 4c0 3 4 8 4 8s4-5 4-8a4 4 0 0 0-4-4zm0 5.6A1.6 1.6 0 1 1 6 2.4a1.6 1.6 0 0 1 0 3.2z"/></svg>
        <span>level 36 Tindale Court, 58 Harwick<br>St Brisbane QLD 4000</span>
      </li>
      <li class="contact__item">
        <svg class="contact__icon" viewBox="0 0 12 12"><path d="M2.4 0.5 4.3 2.6 3.3 4.1c.7 1.6 2 2.9 3.6 3.6l1.5-1 2.1 1.9-1 2c-.3.6-1 .9-1.7.7C4.5 10.4 1.6 7.5.7 4.2.5 3.5.8 2.8 1.4 2.5z"/></svg>
        <span>+61 7 3287 4419</span>
      </li>
      <li class="contact__item">
        <svg class="contact__icon" viewBox="0 0 12 12"><path d="M3 0h6a1 1 0 0 1 1 1v10a1 1 0 0 1-1 1H3a1 1 0 0 1-1-1V1a1 1 0 0 1 1-1zm.6 1.2v5.6h4.8V1.2zm1 6.8v1h1v-1zm2 0v1h1v-1zm-2 1.6v1h1v-1zm2 0v1h1v-1z"/></svg>
        <span>0471 352 608</span>
      </li>
      <li class="contact__item">
        <svg class="contact__icon" viewBox="0 0 12 12"><path d="M0 2.5h12v7H0zm1 1 5 3.3 5-3.3v-.2H1z"/></svg>
        <span>marcus@quillbrookcapital.com.au</span>
      </li>
    </ul>
  </section>

  <section class="card card--back">
    <div class="brand">Quillbrook<br>Capital</div>
    <div class="web">www.quillbrookcapital.com.au</div>
  </section>

</main>
</body>
</html>
```